Dental Office Needs- Flyer Design for Same Day Crowns

We need a flyer that will explain the benefits of the same day crown from the patient prospective. Not show pictures of the machine that makes the crowns. See attached material for content. The flyer should use the practices PMS colors of Green 562 and Blue 3025. The ad should say to the patient - I want to go this office and get my crown done there.
Updates

Project Deadline Extended Reason: The difference in the time zone between USA and Europe has caused issues. Minor changes still need to be worked out. Added Thursday, July 14, 2016

Target Market(s)

Dental Patients

Industry/Entity Type

Dental

Requirements
Must have
• Call to Action
• Business Address and Business Logo
• Classic Design
• images of a Happy 50 year old Couple
• Gives the benefits of the same day crown
Should not have
• No Images of tooth figures
• No before or after pictures

```html
<!DOCTYPE html>
<html lang="en">
<head>
<meta charset="utf-8">
<title>Brookfield Dental Care – One Visit Crowns Flyer</title>
<link href="https://fonts.googleapis.com/css2?family=Roboto+Condensed:wght@400;700&family=Questrial&family=Noto+Serif&display=swap" rel="stylesheet">
<style>
  :root {
    --teal: #0b8374;
    --teal-light: #cfe3df;
    --navy: #135a8c;
    --navy-deep: #0f4d7a;
    --panel-glow: #6a90c0;
    --ink: #1c4f7c;
    --white: #ffffff;
    --backdrop: #3a3a3a;
  }
  * { box-sizing: border-box; margin: 0; padding: 0; }
  html, body { width: 1200px; height: 1200px; overflow: hidden; }
  body { background: var(--backdrop); position: relative; }

  .flyer {
    position: absolute; left: 170px; top: 60px;
    width: 860px; height: 1080px;
    background: var(--white); overflow: hidden;
    box-shadow: 0 10px 30px rgba(0,0,0,.45);
  }
  .top-band { position: absolute; left: 0; top: 0; width: 100%; height: 36px; background: var(--teal); }
  .top-rule { position: absolute; left: 0; top: 36px; width: 100%; height: 6px; background: var(--teal-light); }

  .goodbye-row { position: absolute; left: 0; top: 58px; width: 100%; height: 150px; display: flex; z-index: 2; }
  .goodbye {
    flex: 1; display: flex; flex-direction: column; align-items: center;
    font-family: "Roboto Condensed", sans-serif; text-transform: uppercase;
  }
  .goodbye + .goodbye { border-left: 2px solid #d8e2e6; }
  .goodbye-title { display: flex; align-items: center; gap: 10px; color: var(--teal); font-size: 38px; line-height: 1; }
  .goodbye-title svg { width: 32px; height: 30px; }
  .goodbye-sub { color: var(--ink); font-size: 23px; line-height: 1.2; text-align: center; margin-top: 6px; padding-left: 30px; }

  .photo {
    position: absolute; left: 330px; top: 215px; width: 530px; height: 470px;
    background:
      radial-gradient(ellipse at 62% 45%, #e7dccf 0%, rgba(231,220,207,0) 55%),
      linear-gradient(90deg, #ffffff 0%, #eceff2 30%, #d7dce1 62%, #e9ecef 100%);
  }

  .headline { position: absolute; left: 40px; top: 245px; width: 400px; text-align: center; z-index: 1; }
  .headline-name { font-family: "Questrial", sans-serif; font-weight: 400; line-height: 1.05; }
  .headline-name .line-1 { display: block; color: var(--navy); font-size: 50px; }
  .headline-name .line-2 { display: block; color: var(--teal); font-size: 54px; }
  .headline-offer { font-family: "Noto Serif", serif; color: var(--ink); font-size: 23px; line-height: 1.3; margin-top: 6px; }

  .wave { position: absolute; left: 0; top: 0; width: 860px; height: 1080px; }

  .bubble-text {
    position: absolute; left: 420px; top: 505px; width: 360px;
    font-family: "Questrial", sans-serif; color: var(--navy); font-size: 32px; line-height: 1.12;
    text-transform: uppercase; text-align: center; white-space: nowrap; transform: rotate(-12deg);
  }

  .benefits {
    position: absolute; left: 60px; top: 705px; width: 410px;
    font-family: "Roboto Condensed", sans-serif; font-weight: 700; color: var(--white);
    font-size: 21px; line-height: 1.38; white-space: nowrap;
  }
  .benefits p + p { margin-top: 24px; }

  .contact-panel {
    position: absolute; left: 478px; top: 700px; width: 382px; height: 300px;
    border-left: 1px solid rgba(255,255,255,.25);
    background: radial-gradient(ellipse at 50% 12%, var(--panel-glow) 0%, rgba(106,144,192,0) 70%);
    text-align: center; color: var(--white);
  }
  .practice-name { font-family: "Noto Serif", serif; color: var(--navy-deep); font-size: 25px; margin-top: 28px; display: flex; align-items: center; justify-content: center; gap: 10px; }
  .practice-name .mark { width: 14px; height: 14px; border-radius: 50%; background: var(--teal); }
  .call-label, .call-number { font-family: "Roboto Condensed", sans-serif; font-weight: 700; line-height: 1; }
  .call-label { font-size: 46px; margin-top: 30px; }
  .call-number { font-size: 54px; margin-top: 4px; }
  .address { font-family: "Roboto Condensed", sans-serif; font-size: 20px; margin-top: 14px; }

  .footer-band {
    position: absolute; left: 0; top: 1000px; width: 100%; height: 80px; background: var(--teal);
    display: flex; align-items: center; justify-content: center;
    font-family: "Roboto Condensed", sans-serif; color: var(--white); font-size: 27px; letter-spacing: 13px;
  }
</style>
</head>
<body>
<main class="flyer">
  <div class="top-band"></div>
  <div class="top-rule"></div>

  <section class="goodbye-row">
    <div class="goodbye">
      <div class="goodbye-title"><svg viewBox="0 0 32 30"><path d="M2 16 L11 26 L30 3" fill="none" stroke="#0b8374" stroke-width="6"/></svg>Good-bye</div>
      <div class="goodbye-sub">Temporary<br>Crown</div>
    </div>
    <div class="goodbye">
      <div class="goodbye-title"><svg viewBox="0 0 32 30"><path d="M2 16 L11 26 L30 3" fill="none" stroke="#0b8374" stroke-width="6"/></svg>Good-bye</div>
      <div class="goodbye-sub">Second<br>Appointment</div>
    </div>
    <div class="goodbye">
      <div class="goodbye-title"><svg viewBox="0 0 32 30"><path d="M2 16 L11 26 L30 3" fill="none" stroke="#0b8374" stroke-width="6"/></svg>Good-bye</div>
      <div class="goodbye-sub">Gooey Mess<br>Imprassions</div>
    </div>
  </section>

  <div class="photo" role="img" aria-label="Photo of a smiling senior couple cheek to cheek, dressed in white"></div>

  <section class="headline">
    <h1 class="headline-name"><span class="line-1">BROOKFIELD</span><span class="line-2">DENTAL CARE</span></h1>
    <p class="headline-offer">is pleased to offer you<br>the Comfort and Convenience<br>of One Visit Crowns</p>
  </section>

  <svg class="wave" viewBox="0 0 860 1080" aria-hidden="true">
    <circle cx="600" cy="560" r="175" fill="#ffffff"/>
    <path d="M0 480 C180 470 330 650 480 672 C620 692 740 640 860 520 L860 1000 L0 1000 Z" fill="#0b8374"/>
    <path d="M0 530 C190 525 330 690 485 702 C625 714 745 668 860 560 L860 1000 L0 1000 Z" fill="#135a8c"/>
  </svg>

  <div class="bubble-text">Find out is<br>Digical Dentistry<br>is right for you!</div>

  <section class="benefits">
    <p>Restorative Dentistry has evolved<br>and now, digital technlogy allows us<br>to take an impression of your teeth<br>with a digital scanner and cerate you<br>crown right in our office.</p>
    <p>When it comes to your next crown,<br>the benefits of Dightal Restoration<br>and up quickly!</p>
  </section>

  <section class="contact-panel">
    <div class="practice-name"><span class="mark"></span>Brookfield Dental Care</div>
    <div class="call-label">CALL US TODAY</div>
    <div class="call-number">555. 014. 0192</div>
    <div class="address">48 W. Lakeview Road, Lakeview, MI</div>
  </section>

  <footer class="footer-band">www.brookfielddentalcare.com</footer>
</main>
</body>
</html>
```